makeup banner

Need a pull up banner design for a freelance makeup artist with minimal information and one picture.
details are:
Glambyroselyn
info@glambyroselyn-studio.net
0437862139
specialising in bridal, photography and special event makeup
instagram - glamby_roselyn
facebook - Glambyroselyn

Industry/Entity Type

Makeup

```html
<!DOCTYPE html>
<html lang="en">
<head>
<meta charset="utf-8">
<title>Glambyroselyn – Pull Up Banner</title>
<link rel="stylesheet" href="https://fonts.googleapis.com/css2?family=Playfair+Display:wght@400;600&family=Roboto:wght@500&display=swap">
<style>
  :root {
    --magenta-bright: #d3318a;
    --magenta: #b81f6f;
    --magenta-deep: #8d1651;
    --plum: #7e1a45;
    --plum-dark: #5e1233;
    --gold: #e0b24e;
    --gold-light: #f6dc8c;
    --white: #ffffff;
    --cyan: #2fa6dc;
    --amber: #f2b01e;
    --fb-pink: #e0338f;
  }
  html, body { margin: 0; padding: 0; overflow: hidden; background: var(--white); }
  .banner {
    position: relative; width: 1200px; height: 2396px; overflow: hidden;
    background: linear-gradient(180deg, var(--plum) 0%, var(--plum-dark) 100%);
    font-family: "Playfair Display", "Times New Roman", serif; color: var(--white);
  }
  .header-band {
    position: absolute; left: 0; top: 0; width: 1200px; height: 700px;
    background: radial-gradient(ellipse 70% 60% at 50% 45%, var(--magenta-bright) 0%, var(--magenta) 50%, var(--magenta-deep) 100%);
  }
  .crown-ornament {
    position: absolute; left: 470px; top: 70px; width: 260px; height: 120px;
    background: radial-gradient(ellipse at 50% 60%, rgba(255,255,255,0.55), rgba(255,255,255,0.15) 70%, transparent 72%);
  }
  .specialties {
    position: absolute; left: 0; top: 232px; width: 1200px; margin: 0;
    text-align: center; font-weight: 400; font-size: 58px; line-height: 65px;
    letter-spacing: 1px; text-transform: uppercase;
  }
  .hero-photo {
    position: absolute; left: 0; top: 700px; width: 1200px; height: 1000px;
    background:
      radial-gradient(ellipse 30% 25% at 85% 15%, #fff6d8 0%, rgba(255,240,200,0) 100%),
      radial-gradient(ellipse 35% 50% at 50% 55%, #e6b98d 0%, rgba(215,170,120,0) 100%),
      linear-gradient(180deg, #c9cba0 0%, #9aa364 40%, #b79a5c 75%, #d7b780 100%);
  }
  .wave { position: absolute; left: 0; top: 1600px; width: 1200px; height: 320px; }
  .brand-name {
    position: absolute; left: 0; top: 1880px; width: 1200px; margin: 0;
    text-align: center; font-weight: 400; font-size: 104px; line-height: 120px;
  }
  .instagram-handle {
    position: absolute; left: 0; top: 2030px; width: 1200px;
    text-align: center; font-size: 34px;
  }
  .divider {
    position: absolute; left: 140px; top: 2118px; width: 920px; height: 2px;
    background: rgba(255,255,255,0.55);
  }
  .contact-list {
    position: absolute; left: 250px; top: 2150px; margin: 0; padding: 0; list-style: none;
    font-family: "Roboto", Arial, sans-serif; font-weight: 500; font-size: 52px;
  }
  .contact-item { display: flex; align-items: center; height: 70px; }
  .contact-icon { width: 50px; height: 50px; margin-right: 22px; flex: none; }
</style>
</head>
<body>
<main class="banner">
  <section class="header-band">
    <div class="crown-ornament" role="img" aria-label="Decorative tiara ornament"></div>
    <h1 class="specialties">Specialising in<br>bridal,<br>photography<br>and<br>special event<br>makeup</h1>
  </section>

  <div class="hero-photo" role="img" aria-label="Photo of a smiling young woman with long hair and a flower crown in a sunlit field"></div>

  <svg class="wave" viewBox="0 0 1200 320" preserveAspectRatio="none" aria-hidden="true">
    <defs>
      <linearGradient id="goldSweep" x1="0" y1="0" x2="1" y2="0">
        <stop offset="0" stop-color="#b9862f"/>
        <stop offset="0.55" stop-color="#f6dc8c"/>
        <stop offset="1" stop-color="#d9a440"/>
      </linearGradient>
      <linearGradient id="pinkSweep" x1="0" y1="0" x2="1" y2="0">
        <stop offset="0" stop-color="#b81f6f"/>
        <stop offset="0.5" stop-color="#d3318a"/>
        <stop offset="1" stop-color="#a31a60"/>
      </linearGradient>
    </defs>
    <path d="M0 40 C 300 10, 560 120, 820 90 C 980 70, 1100 30, 1200 20 L1200 320 L0 320 Z" fill="url(#pinkSweep)"/>
    <path d="M0 170 C 320 110, 620 200, 880 150 C 1020 125, 1120 95, 1200 90 L1200 200 C 1050 200, 900 230, 700 215 C 450 195, 250 170, 0 210 Z" fill="url(#goldSweep)"/>
    <path d="M0 210 C 250 170, 450 195, 700 215 C 900 230, 1050 200, 1200 200 L1200 320 L0 320 Z" fill="#7e1a45"/>
  </svg>

  <h2 class="brand-name">Glambyroselyn</h2>
  <div class="instagram-handle">instagram - glamby_roselyn</div>
  <div class="divider"></div>

  <ul class="contact-list">
    <li class="contact-item">
      <svg class="contact-icon" viewBox="0 0 50 50" aria-hidden="true">
        <circle cx="25" cy="25" r="25" fill="var(--cyan)"/>
        <path d="M17 14 l5 -1 3 7 -3 2 c1.5 3.5 4 6 7 7 l2 -3 7 3 -1 5 c-11 1 -21 -9 -20 -20 z" fill="var(--white)"/>
      </svg>
      0437862139
    </li>
    <li class="contact-item">
      <svg class="contact-icon" viewBox="0 0 50 50" aria-hidden="true">
        <circle cx="25" cy="25" r="25" fill="var(--amber)"/>
        <rect x="13" y="16" width="24" height="18" rx="2" fill="var(--white)"/>
        <path d="M13 17 L25 27 L37 17" fill="none" stroke="var(--amber)" stroke-width="2"/>
      </svg>
      info@glambyroselyn-studio.net
    </li>
    <li class="contact-item">
      <svg class="contact-icon" viewBox="0 0 50 50" aria-hidden="true">
        <circle cx="25" cy="25" r="25" fill="var(--fb-pink)"/>
      </svg>
      Glambyroselyn
    </li>
  </ul>
</main>
</body>
</html>
```